HUSH: Hush Until Stories Happen school library event

I need two poster designs for Hush Until Stories Happen (HUSH) in BC, requested by the PCSMG--Pacific Coast School Media Guild. One should be for elementary students and one for high school. I want the date (Monday, October 26, 2020) and Hush Until Stories Happen. I would like the posters in English and in French. French is : Ferme Ton Écran Maintenant! I'm including last year's posters as examples. I would like to be able to print the poster files on 11x17 paper.

• -The phrase "Hush Until Stories Happen" for the English version; "Ferme Ton Écran Maintenant" for the French version.
-Include the organization name: Pacific Coast School Media Guild
-The date: Monday, October 26, 2020
• I would like the elementary version to be bright and colourful--fun for younger kids. I would like the high school version to be a bit more mature for the older students. Can still be bright and colourful.

```html
<!DOCTYPE html>
<html lang="en">
<head>
<meta charset="utf-8">
<title>HUSH — Hush Until Stories Happen</title>
<link rel="stylesheet" href="https://fonts.googleapis.com/css2?family=Archivo:wght@600;700;800&display=swap">
<style>
  :root {
    --magenta: #c6077e;
    --blue: #0a96da;
    --paper: #f6f5f2;
    --tone-cool: #dfe0e4;
    --tone-warm: #ebe4d6;
  }
  html, body {
    margin: 0;
    padding: 0;
    width: 800px;
    height: 1200px;
    overflow: hidden;
    background: var(--paper);
  }
  .poster {
    position: relative;
    width: 800px;
    height: 1200px;
    overflow: hidden;
    background: var(--paper);
    font-family: "Archivo", "Helvetica Neue", Arial, sans-serif;
  }
  .reader-photo {
    position: absolute;
    inset: 0;
    width: 800px;
    height: 1200px;
  }
  .organisation {
    position: absolute;
    left: 40px;
    top: 128px;
    margin: 0;
    color: var(--magenta);
    font-weight: 700;
    font-size: 17px;
    line-height: 28px;
    letter-spacing: 0.26em;
    text-transform: uppercase;
  }
  .presents {
    position: absolute;
    left: 40px;
    top: 327px;
    margin: 0;
    color: var(--blue);
    font-weight: 700;
    font-size: 17px;
    letter-spacing: 0.3em;
    text-transform: uppercase;
  }
  .headline {
    position: absolute;
    left: 38px;
    top: 446px;
    margin: 0;
    color: var(--magenta);
    font-weight: 800;
    font-size: 88px;
    line-height: 97px;
    letter-spacing: -0.02em;
    text-transform: uppercase;
  }
  .headline span { display: block; }
  .event-date {
    position: absolute;
    left: 40px;
    top: 1034px;
    margin: 0;
    color: var(--blue);
    font-weight: 800;
    font-size: 44px;
    line-height: 45px;
    letter-spacing: -0.03em;
    text-transform: uppercase;
  }
  .event-date span { display: block; }
</style>
</head>
<body>
  <main class="poster">
    <svg class="reader-photo" viewBox="0 0 800 1200" role="img"
         aria-label="Photo: a barefoot reader in rolled-up jeans sits on tall stacks of books, a magazine open on their lap">
      <defs>
        <linearGradient id="photo-tones" x1="0" y1="0" x2="1" y2="1">
          <stop offset="0" stop-color="#f6f5f2"/>
          <stop offset="0.45" stop-color="#f3f2ef"/>
          <stop offset="0.75" stop-color="#dfe0e4"/>
          <stop offset="1" stop-color="#ebe4d6"/>
        </linearGradient>
      </defs>
      <rect x="0" y="0" width="800" height="1200" fill="url(#photo-tones)"/>
    </svg>

    <p class="organisation">Pacific<br>Coast<br>School<br>Media<br>Guild</p>
    <p class="presents">Presents</p>

    <h1 class="headline">
      <span>Hush</span>
      <span>Until</span>
      <span>Stories</span>
      <span>Happen</span>
    </h1>

    <p class="event-date">
      <span>Mon //</span>
      <span>October 26 //</span>
      <span>2020 //</span>
    </p>
  </main>
</body>
</html>
```